Bramble Wren Childcare centre needs a new LED outdoor banner

We need a new outdoor banner for our pre-school. It needs to be around 2440 mm x 1220 mm. It will be lit at night so I need it to stand out. I'm looking for a modern upbeat design. It will have my logo in the middle which is a graduation teddy bear with our name and phone number on it. I'm happy to experiment with different design options as mine is 20 years old. It needs to be colorful, inviting and very "in your face" and child friendly. It will be located near the fence of the property so it will be seen by cars driving by at a speed of around 50KM/H. So it needs to be clear, big bold fonts and bright colors. Thank you!

```html
<!DOCTYPE html>
<html lang="en">
<head>
<meta charset="utf-8">
<title>Bramble Wren Childcare Centre – Outdoor Banner</title>
<link rel="stylesheet" href="https://fonts.googleapis.com/css2?family=Outfit:wght@500;600;800&display=swap">
<style>
  :root {
    --page-bg: #e9e9e9;
    --royal-blue: #1b4f9c;
    --navy-text: #1a2f8f;
    --hot-pink: #e5127d;
    --sky-light: #eaf6fd;
    --sky-mid: #a9daf5;
    --white: #ffffff;
    --ink: #111111;
  }
  * { margin: 0; padding: 0; box-sizing: border-box; }
  html, body {
    width: 1200px; height: 1200px; overflow: hidden;
    background: var(--page-bg);
    font-family: "Outfit", sans-serif;
  }
  .banner {
    position: absolute; left: 40px; top: 320px;
    width: 1120px; height: 560px; overflow: hidden;
  }
  .banner-art { position: absolute; inset: 0; }
  .brand {
    position: absolute; left: 560px; width: 520px; top: 80px;
    text-align: center; color: var(--hot-pink); font-weight: 800;
    line-height: 1;
  }
  .brand-mark {
    display: block; width: 46px; height: 46px; margin: 0 auto 12px;
    border-radius: 50%; background: var(--hot-pink);
  }
  .brand-name { font-size: 74px; letter-spacing: -1px; }
  .brand-sub { font-size: 44px; margin-top: 6px; }
  .age-range {
    position: absolute; left: 560px; width: 520px; top: 276px;
    display: flex; align-items: center; justify-content: center; gap: 12px;
    color: var(--navy-text); font-weight: 600; font-size: 46px; line-height: 1;
  }
  .age-range svg { width: 30px; height: 30px; }
  .hours-pill {
    position: absolute; left: 589px; top: 341px; width: 461px; height: 65px;
    background: var(--hot-pink); border: 3px solid var(--ink); border-radius: 14px;
    color: var(--white); font-weight: 600; font-size: 46px;
    display: flex; align-items: center; justify-content: center; line-height: 1;
  }
  .contact {
    position: absolute; left: 540px; width: 560px; top: 462px;
    color: var(--white); font-weight: 500; font-size: 26px;
    text-align: center; line-height: 37px;
  }
</style>
</head>
<body>
  <main class="banner">
    <svg class="banner-art" viewBox="0 0 1120 560" width="1120" height="560">
      <defs>
        <linearGradient id="skyGradient" x1="0" y1="0" x2="0" y2="1">
          <stop offset="0" stop-color="#9fd6f6"/>
          <stop offset="0.45" stop-color="#f4f1f6"/>
          <stop offset="1" stop-color="#a8d8f3"/>
        </linearGradient>
        <linearGradient id="classroomGradient" x1="0" y1="0" x2="1" y2="1">
          <stop offset="0" stop-color="#e8dcd2"/>
          <stop offset="0.45" stop-color="#3aa6c4"/>
          <stop offset="1" stop-color="#b5563f"/>
        </linearGradient>
      </defs>
      <rect class="sky-backdrop" x="0" y="0" width="1120" height="560" fill="url(#skyGradient)"/>
      <g role="img" aria-label="Photo of a smiling teacher painting with three young children at a classroom table">
        <path d="M0 0 H350 C470 120 520 300 453 560 H0 Z" fill="url(#classroomGradient)"/>
      </g>
      <path class="blue-sweep" d="M350 0 H378 C500 140 555 300 537 441 H1120 V560 H453 C520 300 470 120 350 0 Z" fill="var(--royal-blue)"/>
    </svg>

    <div class="brand">
      <span class="brand-mark"></span>
      <div class="brand-name">Bramble Wren</div>
      <div class="brand-sub">Childcare Centre</div>
    </div>

    <div class="age-range">
      <svg viewBox="0 0 20 20"><path fill="var(--navy-text)" d="M10 0 L12 7 L19 5 L13 10 L19 15 L12 13 L10 20 L8 13 L1 15 L7 10 L1 5 L8 7 Z"/></svg>
      <span>0 - 6 YEARS</span>
      <svg viewBox="0 0 20 20"><path fill="var(--navy-text)" d="M10 0 L12 7 L19 5 L13 10 L19 15 L12 13 L10 20 L8 13 L1 15 L7 10 L1 5 L8 7 Z"/></svg>
    </div>

    <div class="hours-pill">7.30AM - 5.30PM</div>

    <div class="contact">
      <p>18 Orchard Rd, Lindale Park NSW 2000</p>
      <p>02 9000 4812 &nbsp;|&nbsp; A/H 0400 135 702</p>
    </div>
  </main>
</body>
</html>
```